LA Billboard Project for Brisk Lending

We are running three different billboards around LA, and we need someone to take the mock-ups I've created and bring this campaign to life. Whatever wording is on the mock-ups should stay the same in the ads you create, but feel free to get creative with layout and style. I've attached our mock-ups, our style guide, our logo, and the necessary specs for the billboards. If you have any questions, feel free to reach out!

```html
<!DOCTYPE html>
<html lang="en">
<head>
<meta charset="utf-8">
<title>Brisk Lending – Mortgage Made Simple Billboard</title>
<link rel="stylesheet" href="https://fonts.googleapis.com/css2?family=Montserrat:wght@500;600;700;800&display=swap">
<style>
  :root {
    --navy: #14294a;
    --teal: #3dbdc6;
    --yellow: #f5d21a;
    --white: #ffffff;
    --backdrop: #e9edf2;
    --photo-sky: #1b3346;
    --photo-pool: #2bb7c8;
    --photo-lawn: #1e2b1c;
  }
  * { margin: 0; padding: 0; box-sizing: border-box; }
  html, body {
    width: 1200px;
    height: 798px;
    overflow: hidden;
    background: var(--backdrop);
    font-family: "Montserrat", Arial, sans-serif;
  }
  .billboard {
    position: absolute;
    left: 0;
    top: 159px;
    width: 1200px;
    height: 480px;
    overflow: hidden;
  }
  .billboard__shapes {
    position: absolute;
    inset: 0;
    width: 1200px;
    height: 480px;
  }
  .billboard__email {
    position: absolute;
    left: 480px;
    top: 12px;
    width: 680px;
    text-align: center;
    color: var(--white);
    font-weight: 700;
    font-size: 34px;
    letter-spacing: 1px;
  }
  .billboard__brand {
    position: absolute;
    left: 560px;
    top: 112px;
    width: 620px;
    text-align: center;
    color: var(--teal);
    font-weight: 700;
    font-size: 58px;
    letter-spacing: -1px;
    line-height: 1;
  }
  .billboard__headline {
    position: absolute;
    left: 560px;
    top: 214px;
    width: 620px;
    text-align: center;
    color: var(--navy);
    font-weight: 800;
    font-size: 40px;
    line-height: 1.15;
    letter-spacing: 1px;
  }
  .billboard__tagline {
    position: absolute;
    left: 560px;
    top: 322px;
    width: 620px;
    text-align: center;
    color: var(--teal);
    font-weight: 600;
    font-size: 13px;
  }
  .billboard__phone {
    position: absolute;
    left: 700px;
    top: 410px;
    width: 480px;
    text-align: center;
    color: var(--white);
    font-weight: 700;
    font-size: 40px;
    letter-spacing: 2px;
  }
</style>
</head>
<body>
  <section class="billboard">
    <svg class="billboard__shapes" viewBox="0 0 1200 480" xmlns="http://www.w3.org/2000/svg" aria-hidden="false">
      <defs>
        <linearGradient id="photo-tones" x1="0" y1="0" x2="0" y2="1">
          <stop offset="0" stop-color="var(--photo-sky)"/>
          <stop offset="0.55" stop-color="#2a5a6b"/>
          <stop offset="0.72" stop-color="var(--photo-pool)"/>
          <stop offset="0.85" stop-color="var(--photo-lawn)"/>
          <stop offset="1" stop-color="var(--photo-lawn)"/>
        </linearGradient>
      </defs>
      <rect class="panel-navy" x="0" y="0" width="1200" height="480" fill="var(--navy)"/>
      <polygon class="panel-white" points="330,0 1200,0 1200,480 760,480" fill="var(--white)"/>
      <polygon class="band-email" points="345,0 1200,0 1200,72 400,72" fill="var(--navy)"/>
      <polygon class="band-phone" points="680,392 1200,392 1200,480 760,480" fill="var(--navy)"/>
      <polyline class="stripe-yellow" points="0,190 330,-14 772,490" fill="none" stroke="var(--yellow)" stroke-width="14"/>
      <polyline class="stripe-teal" points="0,205 330,4 754,490" fill="none" stroke="var(--teal)" stroke-width="10"/>
      <g role="img" aria-label="Photo of a modern luxury home at dusk with a lit glass facade and a turquoise pool">
        <polygon class="house-photo" points="0,214 330,16 742,480 0,480" fill="url(#photo-tones)"/>
      </g>
    </svg>

    <p class="billboard__email">help@brisklending.com</p>
    <p class="billboard__brand">Brisk Lending</p>
    <h1 class="billboard__headline">MORTGAGE MADE<br>SIMPLE</h1>
    <p class="billboard__tagline">Close Faster, With Greater Transparency And Certainty.</p>
    <p class="billboard__phone">800-555-0148</p>
  </section>
</body>
</html>
```